Torvane Travel Business Card Design

We need a new business card design for our travel agency business - Torvane Travel. We design packages to some of the most popular travel destinations in the world for groups, individuals and also tailor-make personalised packages. Our logo attached must be used. On the back of the card we would like a list of all websites under our Torvane brand to be posted. We would like clean, modern, simple design.

Industry/Entity Type

Travel Agent

Contact Information for Business Card

Owen Pridmore
National Sales Manager
Reservations: 1300 742 689
Tel: 61 28473 5096
Fax: 61 2847 3971
Email: owen@torvanetravel.com.au
Web: www.torvanetravel.com.au

Address: Level 1, 417 Harwick Street
Sydney NSW 2000 Australia

Requirements
Must have
• On the back of the card we want all websites listed under our Torvane brand.
• Torvane Travel Group - Wholesale Specialists
• www.qpjourneys.com.au - New Caledonia
• www.bravelmijourneys.com.au - Tahiti
• www.sorvenbreakhub.com.au - China
Nice to have
• Modern, clean lined, simple and fresh
Should not have
• Look dull

```html
<!DOCTYPE html>
<html lang="en">
<head>
<meta charset="utf-8">
<title>Torvane Travel Business Card</title>
<link rel="stylesheet" href="https://fonts.googleapis.com/css2?family=Open+Sans:wght@400;600;700&display=swap">
<style>
  :root {
    --brand-red: #e71d25;
    --brand-navy: #23237a;
    --ink: #333338;
    --card: #ffffff;
    --backdrop: #e9e6e3;
  }
  * { margin: 0; padding: 0; box-sizing: border-box; }
  html, body { width: 1200px; height: 900px; overflow: hidden; }
  body {
    background: var(--backdrop);
    font-family: "Open Sans", Arial, sans-serif;
    color: var(--ink);
    position: relative;
  }
  .card {
    position: absolute;
    height: 344px;
    background: var(--card);
    box-shadow: 0 6px 18px rgba(0,0,0,0.18);
    overflow: hidden;
  }
  .card--front { left: 238px; top: 60px; width: 556px; }
  .card--back { left: 458px; top: 518px; width: 559px; }

  .front__swoosh { position: absolute; inset: 0; width: 100%; height: 100%; }

  .contact { position: absolute; left: 45px; top: 34px; font-size: 14px; line-height: 20px; }
  .contact__name { font-size: 17px; font-weight: 600; color: var(--brand-navy); line-height: 22px; }
  .contact__name .surname { color: var(--brand-red); }
  .contact__title { margin-bottom: 12px; }
  .contact__address { margin-bottom: 14px; }
  .contact__label { color: var(--brand-red); }
  .contact__line { display: flex; align-items: center; gap: 8px; }
  .contact__line svg { width: 11px; height: 11px; flex: none; }

  .front__name {
    position: absolute; right: 28px; bottom: 36px;
    color: #fff; font-size: 34px; font-weight: 600; line-height: 40px; letter-spacing: -0.5px;
  }

  .back__brand { position: absolute; right: 39px; top: 62px; text-align: right; }
  .back__name { font-size: 46px; font-weight: 600; color: var(--brand-navy); line-height: 56px; letter-spacing: -0.5px; }
  .back__division { margin-top: 40px; font-size: 17px; font-weight: 600; color: var(--brand-red); line-height: 22px; }

  .sites { position: absolute; left: 40px; top: 196px; list-style: none; font-size: 15px; line-height: 20px; }
  .sites__region { font-weight: 600; color: var(--brand-navy); }
  .sites__url { color: var(--brand-red); }
</style>
</head>
<body>

<section class="card card--front" aria-label="Business card front">
  <svg class="front__swoosh" viewBox="0 0 556 344" preserveAspectRatio="none" aria-hidden="true">
    <path d="M40 344 C 200 330 330 270 405 150 L 540 0 L556 0 L556 344 Z" fill="var(--brand-red)"/>
    <path d="M40 343 C 200 329 328 268 402 152" fill="none" stroke="var(--brand-navy)" stroke-width="4"/>
  </svg>

  <div class="contact">
    <p class="contact__name">Owen <span class="surname">Pridmore</span></p>
    <p class="contact__title">National Sales Manager</p>
    <p class="contact__address">Level 1, 417 Harwick Street<br>Sydney NSW 2000 Australia</p>
    <p><span class="contact__label">Reservations:</span> 1300 742 689</p>
    <p class="contact__line">
      <svg viewBox="0 0 12 12" aria-label="Phone"><path d="M1 4 Q6 0 11 4 L9 6 L7 5 L5 5 L3 6 Z M2 7 H10 V11 H2 Z" fill="var(--brand-red)"/></svg>
      61 28473 5096</p>
    <p class="contact__line">
      <svg viewBox="0 0 12 12" aria-label="Fax"><rect x="3" y="1" width="6" height="4" fill="none" stroke="var(--brand-red)" stroke-width="1.3"/><rect x="1" y="5" width="10" height="6" rx="1" fill="var(--brand-red)"/></svg>
      61 2847 3971</p>
    <p class="contact__line">
      <svg viewBox="0 0 12 12" aria-label="Email"><rect x="1" y="2.5" width="10" height="7" fill="var(--brand-red)"/><path d="M1 2.5 L6 6.5 L11 2.5" fill="none" stroke="#fff" stroke-width="1"/></svg>
      owen@torvanetravel.com.au</p>
    <p class="contact__line">
      <svg viewBox="0 0 12 12" aria-label="Website"><path d="M5 7 L7 5 M4.5 5.5 L2.5 7.5 A1.8 1.8 0 0 0 4.5 9.5 L6.5 7.5 M7.5 6.5 L9.5 4.5 A1.8 1.8 0 0 0 7.5 2.5 L5.5 4.5" fill="none" stroke="var(--brand-red)" stroke-width="1.3" stroke-linecap="round"/></svg>
      www.torvanetravel.com.au</p>
  </div>

  <p class="front__name">Torvane Travel</p>
</section>

<section class="card card--back" aria-label="Business card back">
  <div class="back__brand">
    <p class="back__name">Torvane Travel</p>
    <p class="back__division">Wholesale Specialists</p>
  </div>

  <ul class="sites">
    <li class="sites__region">New Caledonia</li>
    <li class="sites__url">www.qpjourneys.com.au</li>
    <li class="sites__region">Tahiti</li>
    <li class="sites__url">www.bravelmijourneys.com.au</li>
    <li class="sites__region">China</li>
    <li class="sites__url">www.sorvenbreakhub.com.au</li>
  </ul>
</section>

</body>
</html>
```